Business card design only (Have Logo Online) Shoudl be quick and easy for designer

We would like to have a business card design that is in-line with our company logo. Final deliverables should include two EPS extension file. One for the front card design and the other the back-end design. Please also indicate the font style used.

Advisory Pebbles is a social enterprise that focuses on utilizing technology, unique methodologies and international partnerships to provide a one-stop location for economical and dependable IT-related solutions.

Target Market(s)

Micro, small and medium business owners.

Industry/Entity Type

Business

Requirements
Must have
• The business card should incorporate our company logo.
Nice to have
• A little web 2.0 style would be nice but I haven''t decided yet.

```html
<!DOCTYPE html>
<html lang="en">
<head>
<meta charset="utf-8">
<title>Advisory Pebbles – Business Card</title>
<link rel="stylesheet" href="https://fonts.googleapis.com/css2?family=Open+Sans:wght@600;700&display=swap">
<style>
  :root {
    --page: #ffffff;
    --charcoal: #4a4a4a;
    --charcoal-deep: #3e3e3e;
    --pattern-green: #7fa873;
    --tab-outline: #3a3a3a;
    --brand-green: #3f8a4a;
    --leaf-light: #c9e4b4;
    --frame-green: #3f8a4a;
    --wash: #eef5e9;
    --ink: #1c1c1c;
  }
  html, body {
    margin: 0;
    width: 1056px;
    height: 1200px;
    overflow: hidden;
    background: var(--page);
    font-family: "Open Sans", Arial, sans-serif;
  }
  .canvas { position: relative; width: 1056px; height: 1200px; }

  .card { position: absolute; left: 40px; width: 976px; overflow: hidden; }
  .card--front { top: 24px; height: 563px; background: var(--charcoal); }
  .card--back { top: 630px; height: 545px; background: var(--page); outline: 1px solid #e2e2e2; }

  .pattern-fill { position: absolute; inset: 0; }
  .card--front .pattern-fill {
    background:
      radial-gradient(ellipse 60% 55% at 20% 70%, rgba(127,168,115,0.28) 0%, rgba(127,168,115,0) 100%),
      radial-gradient(ellipse 55% 60% at 82% 35%, rgba(201,228,180,0.22) 0%, rgba(201,228,180,0) 100%),
      radial-gradient(ellipse 50% 45% at 55% 95%, rgba(127,168,115,0.20) 0%, rgba(127,168,115,0) 100%),
      linear-gradient(160deg, var(--charcoal) 0%, #555a53 50%, var(--charcoal-deep) 100%);
  }
  .card--back .pattern-fill {
    background:
      radial-gradient(ellipse 70% 60% at 75% 40%, rgba(201,228,180,0.35) 0%, rgba(201,228,180,0) 100%),
      linear-gradient(180deg, var(--wash) 0%, #fbfdf9 100%);
  }

  .brand-tab { position: absolute; left: 253px; top: -2px; width: 472px; height: 282px; }
  .brand-lockup {
    position: absolute; left: 253px; top: 150px; width: 472px;
    display: flex; align-items: center; justify-content: center; gap: 16px;
  }
  .brand-dot {
    width: 58px; height: 58px; border-radius: 50%;
    background: var(--leaf-light);
  }
  .brand-name {
    font-weight: 700; font-size: 34px; letter-spacing: 1px;
    color: var(--brand-green); text-transform: uppercase;
  }

  .frame {
    position: absolute; left: 13px; top: 17px; right: 18px; bottom: 17px;
    border: 3px solid var(--frame-green);
  }
  .person { position: absolute; left: 79px; top: 250px; color: var(--ink); }
  .person-name { margin: 0; font-size: 30px; font-weight: 700; letter-spacing: 0.5px; }
  .person-title { margin: 6px 0 0 3px; font-size: 18px; font-weight: 700; }

  .contact {
    position: absolute; left: 79px; top: 382px; margin: 0; padding: 0;
    list-style: none; color: var(--ink); font-size: 17.5px; font-weight: 700;
    line-height: 29px; text-transform: uppercase;
  }
  .contact li:first-child { padding-left: 4px; }
</style>
</head>
<body>
<div class="canvas">

  <section class="card card--front" aria-label="Card front">
    <div class="pattern-fill" role="img" aria-label="Repeating pattern of the company emblem in soft greens on charcoal"></div>
    <svg class="brand-tab" viewBox="0 0 472 282" aria-hidden="true">
      <path d="M4 0 V232 Q4 250 24 254 Q236 290 448 254 Q468 250 468 232 V0 Z"
            fill="#ffffff" stroke="var(--tab-outline)" stroke-width="3"/>
    </svg>
    <div class="brand-lockup">
      <span class="brand-dot"></span>
      <span class="brand-name">Advisory Pebbles</span>
    </div>
  </section>

  <section class="card card--back" aria-label="Card back">
    <div class="pattern-fill" role="img" aria-label="Faint repeating pattern of the company emblem"></div>
    <div class="frame"></div>
    <div class="person">
      <h1 class="person-name">THOMAS WHITFIELD</h1>
      <p class="person-title">MANAGING DIRECTOR</p>
    </div>
    <ul class="contact">
      <li>48 Harbor Lane &nbsp; Suite #9 &nbsp;| &nbsp;Riverton, ME 04512 &nbsp;|</li>
      <li>Phone: (555) 018-274 &nbsp;| &nbsp;Fax: (555) 018-2750 &nbsp;|</li>
      <li>Email: tw@advisorypebbles.com &nbsp;| &nbsp;www.advisorypebbles.com &nbsp;|</li>
    </ul>
  </section>

</div>
</body>
</html>
```